Gym Menu

Hi,

I would like to create a menu for my fitness center/ Dance school.

I do have a picture of how i would like it to look like ill attach it down there and instead of the Mexican looking icons i would like to have gym related icons example (Bar bell, dumbbells, etc..)

The menu will consist of the following

Smoothies
- Lagoon Waltz (20 SR)
(Kiwi, Pineapple, Banana, Grapes)
-Coral Drift (20 SR)
(Orange, Peach, Pineapple)
-Tidy Kick (20 SR)
(Carrot, Mango, Orange)
-Purple Thunder (20 SR)
(Blackberry, Raspberry, Banana)
-Cool Breeze (20 SR)
( Lemonade, Mint)
-Ruby Lantern (20 SR)
(Lemonade, Strawberry, Mint)

Mean Green Juices

-Quick Sprout (20SR)
(Cucumber, Celery, Green Apple, Spinach, Lemon, Ginger)
-Hop To It Now! (20 SR)
(Carrots, Apple, Beetroot)

Shake It Up

-Dusky Swirl (20 SR)
(Mocha, Skimmed Milk)

- Velvet Tumbler
(Chocolate, Skimmed Milk)

-Big Lift Zest

(Peanut Butter, Honey, Skimmed Milk, Banana) (20 SR)

Yummy Bites

- Zataar Croissant (10 SR)
- Cheese Croissant (10 SR)
- Plane Croissant (10 SR)
- Blueberry Muffin (7 SR)
- Chocolate Muffin (7 SR)
- Vanilla Muffin (7SR)
- Cookies (7 SR)
- Brownie (10 SR)
-Fresh Berry Popsicle (10 SR)
- Fresh Orange Popsicle (10 SR)

Make it Lite

-Garden Salad (15 SR)
-Greek Salad (15 SR)
-Ceaser Salad (15 SR)
-Italian Salad (15 SR)
- Tuna Sandwich (25 SR)
- Turkey Sandwich (25 SR)
- Chicken Sandwich (25 SR)
-Happy Patch Bowls (8SR)
- Mixed Nuts (10 SR)

Coffee and tea
- Americano (10 SR)
- Espresso (10 SR)
- Turkish Coffee (10 SR)
- Cappuccino (15 SR)
- Cafe Latte (15 SR)
-Hot Cacao (15 SR)
-Extra shor + 5SR

- Green Tea (10 SR)
- Earl Grey (10 SR)
- English Breakfast (10SR)

• The gyms color is orange ... i want this to be in the menu

the gyms name is vartomel i also want this in big somewhere

Colors of the menu should be

Orange
Yellow
green
red

all shades

```html
<!DOCTYPE html>
<html lang="en">
<head>
<meta charset="utf-8">
<title>Vartomel Café Menu</title>
<link href="https://fonts.googleapis.com/css2?family=Alfa+Slab+One&family=Crete+Round&display=swap" rel="stylesheet">
<style>
:root{
  --kraft:#d9b993;
  --kraft-dark:#c9a57c;
  --green:#5cf23a;
  --orange:#f7941d;
  --orange-red:#f15a24;
  --red:#c1001f;
  --yellow:#fcc419;
  --white:#ffffff;
  --rule:#8a7a68;
}
*{margin:0;padding:0;box-sizing:border-box}
html,body{width:1200px;height:755px;overflow:hidden;background:var(--white)}
.canvas{position:relative;width:1200px;height:755px;overflow:hidden;background:var(--white)}
.menu{position:absolute;left:0;top:0;width:940px;height:592px;transform:scale(1.2766);transform-origin:0 0}
.paper{position:absolute;left:0;top:0;width:843px;height:592px;
  background:radial-gradient(ellipse at 30% 20%,#e0c29e 0%,var(--kraft) 50%,var(--kraft-dark) 100%)}
.frames{position:absolute;left:0;top:0;width:843px;height:592px}
.title{position:absolute;font-family:"Alfa Slab One",serif;text-transform:uppercase;white-space:nowrap;font-weight:400}
.list{position:absolute;font-family:"Crete Round",serif;font-size:10.5px;line-height:14.6px}
.item{position:relative}
.price{position:absolute;top:0}
.smoothies-title{left:34px;top:24px;font-size:60px;line-height:66px;color:var(--green)}
.smoothie-list{left:207px;top:32px;width:175px;color:var(--green)}
.smoothie-list .price{left:143px}
.shake-title{left:29px;top:258px;font-size:44px;line-height:56px;color:var(--red)}
.shake-u{left:232px;top:296px;font-size:92px;line-height:92px;color:var(--red)}
.shake-p{left:290px;top:244px;font-size:132px;line-height:132px;color:var(--red)}
.shake-list{left:30px;top:310px;width:290px;color:var(--red)}
.shake-list .price{left:148px}
.shake-list .gap{height:14px}
.juice-title{left:30px;top:450px;font-size:34px;line-height:46px;color:var(--orange-red)}
.juice-list{left:190px;top:497px;width:190px;color:var(--green)}
.juice-list .price{left:160px}
.bites-title{left:460px;top:24px;font-size:38px;line-height:43px;color:var(--red)}
.bites-list{left:615px;top:68px;width:200px;color:var(--red)}
.bites-list .price{left:153px}
.lite-title{left:452px;top:253px;font-size:46px;line-height:51px;color:var(--orange-red)}
.lite-list{left:645px;top:263px;width:160px;color:var(--red)}
.lite-list .price{left:117px}
.coffee-title{left:527px;top:432px;font-size:19px;color:var(--red)}
.coffee-list{top:467px;width:150px;color:var(--red)}
.coffee-left{left:463px}
.coffee-left .price{left:109px}
.coffee-right{left:645px}
.coffee-right .price{left:118px}
.art{position:absolute}
.brand{position:absolute;left:1100px;top:378px;font-family:"Alfa Slab One",serif;font-size:64px;line-height:1;color:var(--orange);
  white-space:nowrap;transform:translate(-50%,-50%) rotate(-90deg)}
</style>
</head>
<body>
<div class="canvas">
 <div class="menu">
  <div class="paper"></div>

  <svg class="frames" viewBox="0 0 843 592" aria-hidden="true">
   <line x1="423" y1="0" x2="423" y2="592" stroke="var(--rule)" stroke-width="1"/>
   <g fill="none" stroke-width="5" stroke-linejoin="miter">
    <path d="M24 20 L393 20 L393 240 L24 245 Z" stroke="var(--orange)"/>
    <path d="M360 247 L395 243" stroke="var(--orange)"/>
    <path d="M24 444 L390 442 L389 578 L24 580 Z" stroke="var(--green)" opacity=".85"/>
    <path d="M446 19 L829 17 L829 226 L590 227 L590 82" stroke="var(--yellow)"/>
    <path d="M438 246 L813 244 L812 408 L438 412 Z" stroke="var(--green)" opacity=".9"/>
   </g>
  </svg>

  <section class="smoothies">
   <h2 class="title smoothies-title">Smo<br>oth<br>ies</h2>
   <div class="list smoothie-list">
    <div class="item">-Lagoon Waltz<br>(Kiwi, Pineapple, Banana,<br>Grapes)<span class="price">20 SR</span></div>
    <div class="item">-Coral Drift<br>(Orange, Peach, Pineapple)<span class="price">20 SR</span></div>
    <div class="item">-Tidy Kick<br>(Carrot, Mango, Orange)<span class="price">20SR</span></div>
    <div class="item">-Purple Thunder<br>(Blackberry, Raspberry,<br>Banana)<span class="price">20SR</span></div>
    <div class="item">-Cool Breeze<br>( Lemonade, Mint)<span class="price">20 SR</span></div>
    <div class="item">-Ruby Lantern<br>(Lemonade, Strawberry, Mint)<span class="price">20 SR</span></div>
   </div>
  </section>

  <section class="shakes">
   <h2 class="title shake-title">Shake It</h2>
   <div class="title shake-u" aria-hidden="true">U</div>
   <div class="title shake-p" aria-hidden="true">P</div>
   <div class="list shake-list">
    <div class="item">-Dusky Swirl<br>(Mocha, Skimmed Milk)<span class="price">20 SR</span></div>
    <div class="gap"></div>
    <div class="item">-Velvet Tumbler<br>(Chocolate, Skimmed Milk)<span class="price">20 SR</span></div>
    <div class="gap"></div>
    <div class="item">-Big Lift Zest<br>(Peanut Butter, Honey, Skimmed Milk, Banana)<span class="price">20 SR</span></div>
   </div>
  </section>

  <section class="juices">
   <h2 class="title juice-title">Mean Green<br>Juices</h2>
   <div class="list juice-list">
    <div class="item">-Quick Sprout<br>(Cucumber, Celery, Green Apple,<br>Spinach, Lemon, Ginger)<span class="price">20 SR</span></div>
    <div class="item">-Hop To It Now!<br>(Carrots, Apple, Beetroot)<span class="price">20 SR</span></div>
   </div>
  </section>

  <section class="bites">
   <h2 class="title bites-title">Yummy<br>Bites</h2>
   <div class="list bites-list">
    <div class="item">- Zataar Croissant<span class="price">10 SR</span></div>
    <div class="item">- Cheese Croissant<span class="price">10 SR</span></div>
    <div class="item">- Plane Croissant<span class="price">10 SR</span></div>
    <div class="item">- Blueberry Muffin<span class="price">&nbsp;&nbsp;7 SR</span></div>
    <div class="item">- Chocolate Muffin<span class="price">&nbsp;&nbsp;7 SR</span></div>
    <div class="item">- Vanilla Muffin<span class="price">&nbsp;&nbsp;7 SR</span></div>
    <div class="item">- Cookies<span class="price">&nbsp;&nbsp;7 SR</span></div>
    <div class="item">- Brownie<span class="price">10 SR</span></div>
    <div class="item">-Fresh Berry Popsicle<span class="price">10 SR</span></div>
    <div class="item">- Fresh Orange Popsicle<span class="price">10 SR</span></div>
   </div>
   <svg class="art" style="left:470px;top:140px" width="82" height="88" viewBox="0 0 82 88" role="img" aria-label="Drink glasses illustration">
    <defs><linearGradient id="glassTone" x1="0" y1="0" x2="1" y2="1"><stop offset="0" stop-color="#c1001f"/><stop offset=".55" stop-color="#f15a24"/><stop offset="1" stop-color="#5cf23a"/></linearGradient></defs>
    <rect width="82" height="88" fill="url(#glassTone)"/>
   </svg>
  </section>

  <section class="lite">
   <h2 class="title lite-title">Make<br>It<br>Lite</h2>
   <div class="list lite-list">
    <div class="item">-Garden Salad<span class="price">15 SR</span></div>
    <div class="item">-Greek Salad<span class="price">15 SR</span></div>
    <div class="item">-Ceaser Salad<span class="price">15 SR</span></div>
    <div class="item">-Italian Salad<span class="price">15 SR</span></div>
    <div class="item">&nbsp;- Tuna Sandwich<span class="price">25 SR</span></div>
    <div class="item">&nbsp;- Turkey Sandwich<span class="price">25 SR</span></div>
    <div class="item">&nbsp;- Chicken Sandwich<span class="price">25 SR</span></div>
    <div class="item">-Happy Patch Bowls<span class="price">&nbsp;&nbsp;8 SR</span></div>
    <div class="item">&nbsp;- Mixed Nuts<span class="price">10 SR</span></div>
   </div>
  </section>

  <section class="coffee">
   <h2 class="title coffee-title">Coffee &amp; Tea</h2>
   <div class="list coffee-list coffee-left">
    <div class="item">- Americano<span class="price">10 SR</span></div>
    <div class="item">- Espresso<span class="price">10 SR</span></div>
    <div class="item">- Turkish Coffee<span class="price">10 SR</span></div>
    <div class="item">- Cappuccino<span class="price">15 SR</span></div>
    <div class="item">- Cafe Latte<span class="price">15 SR</span></div>
    <div class="item">-Hot Cacao<span class="price">15 SR</span></div>
    <div class="item">-Extra shor<span class="price">+ 5 SR</span></div>
   </div>
   <div class="list coffee-list coffee-right">
    <div class="item">- Green Tea<span class="price">10 SR</span></div>
    <div class="item">- Earl Grey<span class="price">10 SR</span></div>
    <div class="item">- English Breakfast<span class="price">10 SR</span></div>
   </div>
   <svg class="art" style="left:624px;top:520px" width="178" height="60" viewBox="0 0 178 60" role="img" aria-label="Cups and teapot illustration">
    <defs><linearGradient id="cupTone" x1="0" y1="0" x2="1" y2="0"><stop offset="0" stop-color="#5cf23a"/><stop offset=".35" stop-color="#c1001f"/><stop offset=".6" stop-color="#fcc419"/><stop offset="1" stop-color="#f15a24"/></linearGradient></defs>
    <rect width="178" height="60" fill="url(#cupTone)"/>
   </svg>
  </section>
 </div>
 <div class="brand">vartomel</div>
</div>
</body>
</html>
```